Funhaven - launching a new children's entertainment venue

Create a flyer (to be used online and offline) to promote a new business

Business name (tbc). Current considerations are:
# "Bramblewood for KIDS"
# "BW for KIDS"
# "BW Parties"

Concept
# A creative play space for young children
# To be used for either (i) birthday parties or (ii) general play area available for Mums/parents groups to hire

Facilities:
# General play space
# Basketball, soccer
# Ball pit
# Video games
# Movies

Room designed for 2-8 year olds in mind

Catering available:
# Party pies, sausage rolls and mini franks
# Potato chips
# Cordial and water
Note - cake not included
Kitchen facility available.

Party host

Use of parents retreat room

Packages (costs):
# 2 hour party with catering pack and host $220 (up to 10 children, $17.50 per child for additional children)
# 2 hour party - BYO and host $200 (up to 10 children, $15 per child for additional children)
# Casual hire (exclusive use of room and parents retreat) - $50 per hour

Note - we also require a new logo for this new business concept

Existing business is called Bramblewood Sports, a basketball training and development facility. The new business needs to be linked to Bramblewood Sports from a banding perspective although does require its own identity

Brand essence - fun, vibrant, colourful, engaging
Updates

Project Deadline Extended Reason: Due to other projects we have been unable to review designs until tomorrow. Therefore we have opened deadline date. Added Monday, October 10, 2016

Target Market(s)

Mums of children aged 2-8 years

Industry/Entity Type

Entertainment

Logo Text

Name "Bramblewood for KIDS" (although name is not 100% confirmed)

Font styles to use
Serif
Sans Serif

Requirements
Must have
• Must be vibrant, colourful and fun
• Get across sense of energy
Nice to have
• Some sort of link to existing business "Bramblewood Sports" logos are attached
• Although we have an open mind to a totally seperate brand

```html
<!DOCTYPE html>
<html lang="en">
<head>
<meta charset="utf-8">
<title>Bramblewood for KIDS – Flyer</title>
<link rel="stylesheet" href="https://fonts.googleapis.com/css2?family=Alfa+Slab+One&family=Baloo+2:wght@500;600;700&family=Courgette&family=Open+Sans:wght@600&family=Oswald:wght@600&display=swap">
<style>
  :root{
    --board:#5c1013;
    --board-text:#b89a9a;
    --red:#e62a27;
    --panel-green:#37402a;
    --panel-border:#6d6a2c;
    --panel-brown:#4b3f2c;
    --room-brown:#8a4a1d;
    --gold:#f5d23a;
    --orange:#ff8a1e;
    --olive:#6e7a27;
    --white:#ffffff;
    --ink:#111111;
  }
  *{box-sizing:border-box;margin:0;padding:0}
  html,body{width:1200px;height:1200px;overflow:hidden;background:var(--board)}
  .board{position:relative;width:1200px;height:1200px}
  .board-title{position:absolute;top:14px;width:100%;text-align:center;font-family:"Open Sans",sans-serif;font-weight:600;color:var(--board-text);font-size:36px;letter-spacing:1px}
  .board-sub{position:absolute;top:60px;width:100%;text-align:center;font-family:"Open Sans",sans-serif;font-weight:600;color:var(--board-text);font-size:24px}

  .flyer{position:absolute;left:182px;top:110px;width:932px;height:1338px;transform:scale(.8);transform-origin:0 0;background:var(--red);overflow:hidden;font-family:"Baloo 2",sans-serif;font-weight:600}
  .top-band{position:absolute;left:0;top:0;width:100%;height:125px;background:linear-gradient(#7d7d7b,#a4a4a2)}
  .headline{position:absolute;left:32px;top:48px;width:680px;white-space:nowrap;font-family:"Alfa Slab One",serif;font-weight:400;font-size:39px;letter-spacing:.5px;background:linear-gradient(#f3ea2c,#7fc23a);-webkit-background-clip:text;background-clip:text;-webkit-text-fill-color:transparent;text-transform:uppercase}
  .brand-box{position:absolute;left:736px;top:33px;width:158px;height:165px;background:var(--ink);display:flex;align-items:flex-end;justify-content:center;padding-bottom:26px;z-index:3}
  .brand-name{font-weight:700;color:var(--white);font-size:21px;text-align:center;line-height:1.05}

  .hero-photo{position:absolute;left:0;top:120px;width:100%;height:530px;background:linear-gradient(180deg,#cfcfcf 0%,#d9c76a 30%,#c8343a 45%,#3e6a2e 70%,#2f5726 100%);clip-path:polygon(0 0,100% 0,100% 76%,50% 100%,0 78%)}

  .thumb{position:absolute;background:var(--white);padding:7px;box-shadow:0 3px 6px rgba(0,0,0,.35)}
  .thumb span{display:block;width:100%;height:100%}
  .t1{left:35px;top:605px;width:158px;height:165px;transform:rotate(-9deg)}
  .t1 span{background:linear-gradient(#d0d0c8 30%,#40702e)}
  .t2{left:188px;top:628px;width:182px;height:175px;transform:rotate(4deg)}
  .t2 span{background:linear-gradient(#e0c84a,#3a4fa0 60%,#c83a3a)}
  .t3{left:356px;top:622px;width:188px;height:170px;transform:rotate(-5deg)}
  .t3 span{background:linear-gradient(#9a7a55 30%,#d8d0c8 55%,#3e6a2e)}
  .t4{left:535px;top:597px;width:172px;height:166px;transform:rotate(2deg)}
  .t4 span{background:linear-gradient(90deg,#d8c84a,#c8343a 40%,#3e6a2e 70%,#c9c9c4)}
  .t5{left:692px;top:598px;width:175px;height:166px;transform:rotate(-9deg)}
  .t5 span{background:linear-gradient(#cfcfcf 35%,#3e6a2e)}

  .panel{position:absolute;border-radius:10px;color:var(--white);box-shadow:0 5px 0 rgba(120,110,40,.9)}
  .panel-green{background:var(--panel-green);border:3px solid var(--panel-border)}
  .panel-title{font-family:"Courgette",cursive;color:var(--gold);font-size:38px;text-align:center;border-bottom:2px solid var(--gold);display:inline-block;line-height:1.15}
  .ticks{list-style:none;font-size:18px;line-height:23px}
  .ticks li{position:relative;padding-left:22px}
  .ticks li::before{content:"✔";position:absolute;left:0;color:var(--orange)}
  .facilities{left:32px;top:834px;width:237px;height:233px;padding:14px 16px}
  .facilities .panel-title{margin:0 0 24px 28px}
  .catering{left:632px;top:837px;width:270px;height:233px;padding:12px 16px}
  .catering .panel-title{margin:0 0 18px 40px}
  .catering .note{font-size:17px;line-height:19px;margin-top:14px}
  .space-for{left:284px;top:830px;width:333px;height:132px;background:var(--panel-brown);transform:rotate(-2deg);padding:6px 22px}
  .space-for h2{font-weight:700;color:var(--gold);font-size:30px;line-height:1.2;text-align:center;text-decoration:underline;text-underline-offset:4px}
  .space-for p{font-size:18px;line-height:20px;margin-top:6px}
  .room{left:334px;top:965px;width:235px;height:117px;background:var(--room-brown);transform:rotate(1.5deg);text-align:center;padding-top:6px}
  .room .lead{color:var(--gold);font-size:20px;line-height:26px}
  .room .ages{font-weight:700;font-size:38px;line-height:42px}
  .room .tail{color:var(--gold);font-size:20px;line-height:26px}

  .packages{position:absolute;left:34px;top:1088px;width:880px;color:var(--white)}
  .packages h2{font-size:26px;font-weight:700}
  .package-list{list-style:none;margin:8px 0 0 22px;font-size:17px;line-height:25px;color:var(--gold);font-weight:500}
  .package-list li{position:relative;padding-left:24px}
  .package-list li::before{content:"✔";position:absolute;left:0;top:4px;width:16px;height:16px;border-radius:50%;background:var(--ink);color:var(--white);font-size:11px;line-height:16px;text-align:center}
  .package-list b{font-weight:700;color:var(--white)}
  .package-list em{font-style:normal;color:var(--gold);font-weight:700}
  .package-list u{color:var(--gold)}

  .contact-band{position:absolute;left:-80px;top:1208px;width:1092px;height:260px;border-radius:50% 50% 0 0;background:var(--olive)}
  .contact{position:absolute;left:0;top:1226px;width:100%;text-align:center}
  .contact h2{font-weight:600;color:var(--white);font-size:26px;text-decoration:underline;text-underline-offset:5px;opacity:.85}
  .contact .info{font-family:"Oswald",sans-serif;color:var(--gold);font-size:15px;margin-top:10px}
  .contact .phone{font-family:"Oswald",sans-serif;color:var(--gold);font-size:22px;margin-top:2px}
  .contact .phone b{color:var(--white)}
</style>
</head>
<body>
<div class="board">
  <div class="board-title">REVISED DESIGN IDEA - 01</div>
  <div class="board-sub">(Updated with latest images)</div>

  <div class="flyer">
    <div class="top-band"></div>
    <div class="hero-photo" role="img" aria-label="Photo of children playing basketball on artificial turf in a colourful padded play room"></div>
    <h1 class="headline">Bramblewood for Kids</h1>
    <div class="brand-box">
      <div class="brand-name">BRAMBLEWOOD<br>SPORTS</div>
    </div>

    <div class="thumb t1"><span role="img" aria-label="Photo of the play room with ball pit balls on the turf"></span></div>
    <div class="thumb t2"><span role="img" aria-label="Photo of children playing in the ball pit"></span></div>
    <div class="thumb t3"><span role="img" aria-label="Photo of children at a party table eating"></span></div>
    <div class="thumb t4"><span role="img" aria-label="Photo of the empty play room with basketball hoop"></span></div>
    <div class="thumb t5"><span role="img" aria-label="Photo of children playing in the room"></span></div>

    <div class="panel panel-green facilities">
      <div class="panel-title">Facilities</div>
      <ul class="ticks">
        <li>General play space</li>
        <li>Basketball, soccer</li>
        <li>Ball pit</li>
        <li>Video games</li>
        <li>Movies</li>
      </ul>
    </div>

    <div class="panel space-for">
      <h2>Space For</h2>
      <p>i) Birthday Parties (or)</p>
      <p>ii) General play area available for<br>&nbsp;&nbsp;&nbsp;&nbsp;Mums/parents groups to hire.</p>
    </div>

    <div class="panel room">
      <div class="lead">Room designed for</div>
      <div class="ages">2–8yrs</div>
      <div class="tail">old in mind</div>
    </div>

    <div class="panel panel-green catering">
      <div class="panel-title">Catering</div>
      <ul class="ticks">
        <li>Party pies, sausage rolls and mini franks</li>
        <li>Potato chips</li>
        <li>Cordial and water</li>
      </ul>
      <p class="note">Note – cake not included<br>Kitchen facility available.</p>
    </div>

    <div class="packages">
      <h2>Package (Costs) :</h2>
      <ul class="package-list">
        <li><em>2 hour party</em> with catering pack and host <b>$220</b> (up to <u>10 children</u>, <b>$17.50 per child</b> for additional children)</li>
        <li><em>2 hour party</em> – BYO and host <b>$200</b> (up to <u>10 children</u>, <b>$15 per child</b> for additional children)</li>
        <li><em>Casual hire</em> (exclusive use of room and parents retreat) – <b>$50 per hour</b></li>
      </ul>
    </div>

    <div class="contact-band"></div>
    <div class="contact">
      <h2>CONTACT US</h2>
      <p class="info">FOR MORE INFORMATION AND OTHER TRAVEL PACKAGES:</p>
      <p class="phone">PH. 805-555-0142 OR VISIT <b>WWW.BRAMBLEWOODFORKIDS.COM</b></p>
    </div>
  </div>
</div>
</body>
</html>
```